Coaching business needs flyer for business market

I need a flyer that I can send to HR-managers and business owners to inform them of my coaching services for organisations. We have three services: organisational- and teamcoaching, individual coaching and training programs.
I want the flyer to express calmness, solid and trustworthy coaching. As a person I am open and think out of the box.

In my logo I use a couple of colours (blue, green, orange and grey) that represent the diversity of humans. My company's name is Bramblecrest Engagement & Coaching and tag line is "Awaken your quiet river".

I do not want the design to be too busy but also not too boring. I tried making something myself. Feel free to build on that design. Or feel free to start from scratch.

```html
<!DOCTYPE html>
<html lang="nl">
<head>
<meta charset="utf-8">
<title>Bramblecrest Engagement &amp; Coaching – A4 flyer voor- en achterkant</title>
<link rel="stylesheet" href="https://fonts.googleapis.com/css2?family=Montserrat:wght@300;400;500;700;800&display=swap">
<style>
  :root{
    --board:#cfc6c2;
    --board-floor:#c7bdb9;
    --ink-brown:#3b1f16;
    --white:#ffffff;
    --text-grey:#5d5d5f;
    --brand-blue:#1f4f9c;
    --bar-blue:#1d55a5;
    --hex-blue:#3f5cba;
    --teal:#3db3c7;
    --orange:#ec7f2e;
    --red:#c1232c;
    --photo-office:#a9a49d;
    --photo-office-dark:#6d6860;
    --photo-stage:#1d1b22;
    --photo-stage-light:#3c3540;
  }
  *{box-sizing:border-box;margin:0;padding:0}
  html,body{width:1200px;height:447px;overflow:hidden;background:var(--board)}
  body{font-family:"Montserrat",Arial,sans-serif}
  .board{position:relative;width:1200px;height:447px;
    background:linear-gradient(var(--board) 0 389px,var(--board-floor) 389px)}
  .board-title{position:absolute;left:52px;top:38px;font-size:14px;font-weight:700;color:var(--ink-brown)}
  .side-label{position:absolute;top:8px;font-size:13px;font-weight:700;color:var(--ink-brown);transform:translateX(-50%)}

  .flyer{position:absolute;width:274px;height:388px;background:var(--white);overflow:hidden;
    box-shadow:2px 3px 6px rgba(60,40,30,.25)}
  .flyer--small{transform:scale(.752);transform-origin:top left}
  .flyer svg.shapes{position:absolute;inset:0}

  /* brand name block */
  .brand{position:absolute;text-align:center;color:var(--text-grey);font-weight:400}
  .brand-dot{display:block;margin:0 auto 3px;border-radius:50%;border:1.5px solid var(--teal)}
  .brand-name{display:block;line-height:1}
  .brand-tag{display:block;margin-top:2px}

  /* front */
  .front .brand{left:0;top:16px;width:104px}
  .front .brand-dot{width:18px;height:18px}
  .front .brand-name{font-size:14px}
  .front .brand-tag{font-size:6.6px}
  .coach-name{position:absolute;left:8px;top:235px;font-size:8.6px;font-weight:800;color:var(--brand-blue)}
  .coach-bio{position:absolute;left:8px;top:246px;width:262px;font-size:6.1px;line-height:1.17;color:var(--text-grey);font-weight:400}
  .team-heading{position:absolute;left:91px;top:315px;width:180px;font-size:8.3px;line-height:1.18;font-weight:800;color:var(--red)}
  .team-list{position:absolute;left:91px;top:350px;width:182px;font-size:6.2px;line-height:1.35;color:var(--text-grey)}

  ul.dots{list-style:none}
  ul.dots li{position:relative;padding-left:9px}
  ul.dots li::before{content:"";position:absolute;left:1px;top:.45em;width:3.2px;height:3.2px;border-radius:50%;background:var(--red)}
  ul.dots--blue li::before{background:var(--brand-blue)}
  ul.dots--teal li::before{background:var(--teal)}

  /* back */
  .back .individual-heading{position:absolute;left:9px;top:10px;font-size:8.6px;line-height:1.2;font-weight:800;color:var(--brand-blue)}
  .back .individual-list{position:absolute;left:9px;top:35px;width:250px;font-size:6.1px;line-height:1.38;color:var(--white)}
  .back .training-heading{position:absolute;left:8px;top:83px;width:160px;font-size:9.2px;line-height:1.2;font-weight:800;color:var(--teal)}
  .back .training-list{position:absolute;left:9px;top:128px;width:108px;font-size:6.2px;line-height:1.2;color:var(--text-grey)}
  .back .training-list li{margin-bottom:3.5px}
  .back .practice-heading{position:absolute;left:8px;top:183px;width:110px;font-size:9.2px;line-height:1.2;font-weight:800;color:var(--white)}
  .back .practice-list{position:absolute;left:9px;top:237px;width:112px;font-size:6.2px;line-height:1.15;color:var(--text-grey)}
  .back .practice-list li{margin-bottom:4px}
  .back .brand{left:87px;top:306px;width:100px}
  .back .brand-dot{width:22px;height:22px}
  .back .brand-name{font-size:15.5px}
  .back .brand-tag{font-size:7px}
  .contact-bar{position:absolute;left:0;right:0;bottom:0;height:22px;background:var(--bar-blue);
    color:var(--white);font-size:9.6px;font-weight:700;display:flex;align-items:center;justify-content:center}
  .contact-bar span.sep{display:inline-block;width:1px;height:10px;background:var(--white);margin:0 3px}
</style>
</head>
<body>
<main class="board">
  <h1 class="board-title">A4 Size Flyer Front &amp; Back</h1>
  <div class="side-label" style="left:419px">Front</div>
  <div class="side-label" style="left:804px">Back</div>

  <!-- FRONT, small + large share markup -->
  <section class="flyer front flyer--small" style="left:28px;top:102px">
    <svg class="shapes" viewBox="0 0 274 388" width="274" height="388">
      <path role="img" aria-label="Foto: groep deelnemers in gesprek in een lichte vergaderzaal" fill="url(#officeA)" d="M0 0H274V150Q246 190 200 220Q150 250 100 236Q50 222 0 200Z"/>
      <path fill="var(--white)" d="M0 0H107V72Q107 82 97 86L60 97Q53 99 46 97L10 86Q0 82 0 72Z"/>
      <path fill="var(--hex-blue)" stroke="var(--teal)" stroke-width="3" role="img" aria-label="Portretfoto van de coach" d="M210 142L265 173V237L210 268L155 237V173Z"/>
      <rect role="img" aria-label="Foto: teamcoaching-oefening in een groep" x="0" y="310" width="86" height="78" fill="url(#teamA)"/>
      <defs>
        <linearGradient id="officeA" x1="0" y1="0" x2="0" y2="1"><stop offset="0" stop-color="#d7d3cd"/><stop offset=".55" stop-color="var(--photo-office)"/><stop offset="1" stop-color="var(--photo-office-dark)"/></linearGradient>
        <linearGradient id="teamA" x1="0" y1="0" x2="1" y2="1"><stop offset="0" stop-color="#8b7e74"/><stop offset="1" stop-color="#c1b5a4"/></linearGradient>
      </defs>
    </svg>
    <div class="brand"><span class="brand-dot"></span><span class="brand-name">bramblecrest</span><span class="brand-tag">engagement &amp; coaching</span></div>
    <h2 class="coach-name">MIRELLE VANDAAN</h2>
    <p class="coach-bio">is trainer en coach. Ze heeft ruime ervaring met veranderingstrajecten binnen organisaties. Mensen omschrijven haar als ’betrokken, warm, stevig en kordaat’. Het is haar passie om organisaties, teams en mensen te helpen groeien. Zij helpt weerstand te overwinnen en draagt bij aan groei in zelfvertrouwen. Haar trainingen en coaching zijn erop gericht om snel inzichtelijk te krijgen welke stappen men moet zetten om verder te komen. Ze gelooft de veranderkracht van de mensen waar ze mee werkt. Ze is er om steun en richting te bieden en laat hen zelf aan het roer.</p>
    <h3 class="team-heading">Een organisatie waar medewerkers zijn, samenwerken, communiceren door ORGANISATIE- of TEAM coaching:</h3>
    <ul class="team-list dots">
      <li>Heb je zorgen voor of na een fusie of verandering?</li>
      <li>Wil je missie, visie &amp; strategie ontwikkelen of wijzigen?</li>
      <li>Wens je de cultuur-veranderen of verder ontwikkelen?</li>
      <li>Beoog je de samenwerking bevorderen of verbeteren?</li>
    </ul>
  </section>

  <section class="flyer front" style="left:301px;top:33px">
    <svg class="shapes" viewBox="0 0 274 388" width="274" height="388">
      <path role="img" aria-label="Foto: groep deelnemers in gesprek in een lichte vergaderzaal" fill="url(#officeB)" d="M0 0H274V150Q246 190 200 220Q150 250 100 236Q50 222 0 200Z"/>
      <path fill="var(--white)" d="M0 0H107V72Q107 82 97 86L60 97Q53 99 46 97L10 86Q0 82 0 72Z"/>
      <path fill="var(--hex-blue)" stroke="var(--teal)" stroke-width="3" role="img" aria-label="Portretfoto van de coach" d="M210 142L265 173V237L210 268L155 237V173Z"/>
      <rect role="img" aria-label="Foto: teamcoaching-oefening in een groep" x="0" y="310" width="86" height="78" fill="url(#teamB)"/>
      <defs>
        <linearGradient id="officeB" x1="0" y1="0" x2="0" y2="1"><stop offset="0" stop-color="#d7d3cd"/><stop offset=".55" stop-color="var(--photo-office)"/><stop offset="1" stop-color="var(--photo-office-dark)"/></linearGradient>
        <linearGradient id="teamB" x1="0" y1="0" x2="1" y2="1"><stop offset="0" stop-color="#8b7e74"/><stop offset="1" stop-color="#c1b5a4"/></linearGradient>
      </defs>
    </svg>
    <div class="brand"><span class="brand-dot"></span><span class="brand-name">bramblecrest</span><span class="brand-tag">engagement &amp; coaching</span></div>
    <h2 class="coach-name">MIRELLE VANDAAN</h2>
    <p class="coach-bio">is trainer en coach. Ze heeft ruime ervaring met veranderingstrajecten binnen organisaties. Mensen omschrijven haar als ’betrokken, warm, stevig en kordaat’. Het is haar passie om organisaties, teams en mensen te helpen groeien. Zij helpt weerstand te overwinnen en draagt bij aan groei in zelfvertrouwen. Haar trainingen en coaching zijn erop gericht om snel inzichtelijk te krijgen welke stappen men moet zetten om verder te komen. Ze gelooft de veranderkracht van de mensen waar ze mee werkt. Ze is er om steun en richting te bieden en laat hen zelf aan het roer.</p>
    <h3 class="team-heading">Een organisatie waar medewerkers zijn, samenwerken, communiceren door ORGANISATIE- of TEAM coaching:</h3>
    <ul class="team-list dots">
      <li>Heb je zorgen voor of na een fusie of verandering?</li>
      <li>Wil je missie, visie &amp; strategie ontwikkelen of wijzigen?</li>
      <li>Wens je de cultuur-veranderen of verder ontwikkelen?</li>
      <li>Beoog je de samenwerking bevorderen of verbeteren?</li>
    </ul>
  </section>

  <!-- BACK, large + small -->
  <section class="flyer back" style="left:667px;top:33px">
    <svg class="shapes" viewBox="0 0 274 388" width="274" height="388">
      <path fill="var(--orange)" d="M0 0H274V58Q271 64 262 67L212 80H0Z"/>
      <path role="img" aria-label="Foto: deelnemers van een workshop op een donker podium" fill="url(#stageA)" d="M252 70Q264 64 274 72V328L228 352Q218 357 208 351L128 312Q116 305 116 292V172Q116 159 128 152Z"/>
      <path fill="var(--red)" d="M0 179H111L122 229L0 232Z"/>
      <defs><linearGradient id="stageA" x1="0" y1="0" x2="1" y2="1"><stop offset="0" stop-color="var(--photo-stage-light)"/><stop offset="1" stop-color="var(--photo-stage)"/></linearGradient></defs>
    </svg>
    <h2 class="individual-heading">Duurzame Inzetbaarheid door<br>INDIVIDUELE Coaching:</h2>
    <ul class="individual-list dots dots--blue">
      <li>Wens je medewerkers die hun talent ten volste benutten?</li>
      <li>Verlang je meer authentieke leiderschap bij je collega’s?</li>
      <li>Wil je de mensen vooruit helpen in hun loopbaan?</li>
      <li>Zoek je steun voor medewerkers met burn-out of re-integratie?</li>
      <li>Heb je hulp nodig bij outplacement trajecten?</li>
    </ul>
    <h2 class="training-heading">Ontwikkeling &amp; Borging van kennis en vakmanschap door LEERGANGEN, TRAININGEN &amp; WORKSHOPS op MAAT:</h2>
    <ul class="training-list dots dots--teal">
      <li>Leiderschap</li>
      <li>Communicatie</li>
      <li>Leren kijken met ’systemische blik’ voor professionals</li>
      <li>Conflicthantering</li>
    </ul>
    <h2 class="practice-heading">Gedegen resultaat en kwaliteit door bewezen ‘best practices’</h2>
    <ul class="practice-list dots">
      <li>Neuro Linguïstisch Programmeren (NLP)</li>
      <li>Transactionele Analyse</li>
      <li>Systemisch Werken: Organisatieopstellingen, Familieopstellingen, Identity oriented Psycho Traumaopstellingen)</li>
      <li>Somatic Experience, Ademwerk en Lichaamswerk</li>
    </ul>
    <div class="brand"><span class="brand-dot"></span><span class="brand-name">bramblecrest</span><span class="brand-tag">engagement &amp; coaching</span></div>
    <div class="contact-bar">+31-6-12 34 56 78<span class="sep"></span>bramblecrest.nu</div>
  </section>

  <section class="flyer back flyer--small" style="left:961px;top:109px">
    <svg class="shapes" viewBox="0 0 274 388" width="274" height="388">
      <path fill="var(--orange)" d="M0 0H274V58Q271 64 262 67L212 80H0Z"/>
      <path role="img" aria-label="Foto: deelnemers van een workshop op een donker podium" fill="url(#stageB)" d="M252 70Q264 64 274 72V328L228 352Q218 357 208 351L128 312Q116 305 116 292V172Q116 159 128 152Z"/>
      <path fill="var(--red)" d="M0 179H111L122 229L0 232Z"/>
      <defs><linearGradient id="stageB" x1="0" y1="0" x2="1" y2="1"><stop offset="0" stop-color="var(--photo-stage-light)"/><stop offset="1" stop-color="var(--photo-stage)"/></linearGradient></defs>
    </svg>
    <h2 class="individual-heading">Duurzame Inzetbaarheid door<br>INDIVIDUELE Coaching:</h2>
    <ul class="individual-list dots dots--blue">
      <li>Wens je medewerkers die hun talent ten volste benutten?</li>
      <li>Verlang je meer authentieke leiderschap bij je collega’s?</li>
      <li>Wil je de mensen vooruit helpen in hun loopbaan?</li>
      <li>Zoek je steun voor medewerkers met burn-out of re-integratie?</li>
      <li>Heb je hulp nodig bij outplacement trajecten?</li>
    </ul>
    <h2 class="training-heading">Ontwikkeling &amp; Borging van kennis en vakmanschap door LEERGANGEN, TRAININGEN &amp; WORKSHOPS op MAAT:</h2>
    <ul class="training-list dots dots--teal">
      <li>Leiderschap</li>
      <li>Communicatie</li>
      <li>Leren kijken met ’systemische blik’ voor professionals</li>
      <li>Conflicthantering</li>
    </ul>
    <h2 class="practice-heading">Gedegen resultaat en kwaliteit door bewezen ‘best practices’</h2>
    <ul class="practice-list dots">
      <li>Neuro Linguïstisch Programmeren (NLP)</li>
      <li>Transactionele Analyse</li>
      <li>Systemisch Werken: Organisatieopstellingen, Familieopstellingen, Identity oriented Psycho Traumaopstellingen)</li>
      <li>Somatic Experience, Ademwerk en Lichaamswerk</li>
    </ul>
    <div class="brand"><span class="brand-dot"></span><span class="brand-name">bramblecrest</span><span class="brand-tag">engagement &amp; coaching</span></div>
    <div class="contact-bar">+31-6-12 34 56 78<span class="sep"></span>bramblecrest.nu</div>
  </section>
</main>
</body>
</html>
```